SEO and image area for top of invitation website

We need to add an area on our final category pages for SEO text. Instead of just adding text, we'd like to develop a graphical approach that keeps with our soft, feminine look.

You can view an example of our current final category page at http://www.partywren.example/invitations/boy-birthday

I've attached an image of what we're thinking it could look like, but you're welcome to alter the design.

The area should be the same width as our site, but can be any height you determine appropriate.

The winner of this project may be approached to develop the additional designs and backgrounds for us as another project. We additionally have several other projects we're interested in doing with the winner.

We have had a question about the right side of the banner, and what "Free Unlimited Proofs" mean.

About Free Unlimited Proofs:

We are a custom invitation printing company. When a customer orders an invitation from us, they tell us what information we want on the invitation. We then create an electronic sample, or "proof", of what it will look like. We then email it to the customer and they can tell us if they want to make any more changes. We will continue to send them samples, or what we call "proofs", until they are completely satisfied with the way it looks.

We offer Free UNLIMITED Proofs. Compared to our competitors, we are the only one to offer free unlimited proofs.

So, for the right side of this banner, we need an image, or a badge, promoting that we offer free unlimited proofs, and you can include that we are the only ones to do it, if your design has space for that information.

Also, keep in mind, that for other category pages, we may create different images or badges to put in this area - such as for our Low Price Guarantee or to promote a coupon or specific product, for example. So, your design should be able to work with various images on the right side.

Target Market(s)

Our demographic is 100% women, ages 25-60.

Industry/Entity Type

Seo

Requirements
Must have
• The area must have 3 things:
1) Area for the title of the page.
2) Area for SEO text describing the category page.
3) Area for an image. Keep in mind that this image may change for each category page. For this project, you will create an image for our offering of "Free Unlimited Proofs". On other pages, we may display other images we create such as "Low Price Guarantee" or images of certain products we'd like to promote. Just keep this in mind when you're making the design flow.
Nice to have
• Optional: Light design background. We wouldn't mind there being a slight graphical background to this area, to keep it interesting to the eye. Then, for other category pages, we may make additional backgrounds to use in this box area.

```html
<!DOCTYPE html>
<html lang="en">
<head>
<meta charset="utf-8">
<title>Party Wren – Boy Birthday Invitations</title>
<link rel="stylesheet" href="https://fonts.googleapis.com/css2?family=Rokkitt:wght@400;500&family=Signika:wght@600&family=Arimo:wght@400;700&family=Open+Sans:wght@400;600&family=Oswald:wght@700&display=swap">
<style>
:root{
  --ink:#6b5a5f;
  --text:#555;
  --muted:#777;
  --rule:#cfcfcf;
  --bar:#f2f2f2;
  --pink-1:#ffe0fa;
  --pink-2:#f7c0ee;
  --plum:#9a4b94;
  --plum-dark:#5a2a5a;
  --teal:#3aa5a0;
  --gold:#f5c342;
  --featured:#7a6a6d;
  --card:#efefef;
}
*{box-sizing:border-box;margin:0;padding:0}
html,body{width:1200px;height:849px;overflow:hidden;background:#fff}
.page{position:relative;width:1200px;height:849px;overflow:hidden;font-family:"Open Sans",sans-serif;color:var(--text)}
.abs{position:absolute}

/* utility bar */
.utility-bar{left:0;top:0;width:1200px;height:34px;background:var(--bar);border-bottom:1px solid #ddd;font-family:"Signika",sans-serif;font-weight:600;font-size:14px;color:#444}
.utility-item{position:absolute;top:0;height:34px;display:flex;align-items:center;gap:8px}
.utility-sep{position:absolute;top:0;width:1px;height:34px;background:#d6d6d6}

/* header */
.brand{left:24px;top:60px;display:flex;align-items:center;gap:16px}
.brand-mark{width:62px;height:62px;background:var(--featured);border-radius:4px}
.brand-name{font-family:"Rokkitt",serif;font-size:50px;color:var(--ink);line-height:1}
.search{left:458px;top:83px;width:347px;height:53px;border:1px solid #e2e2e2;border-radius:4px;background:#fff;box-shadow:0 0 4px #e8e8e8}
.search-btn{position:absolute;right:7px;top:9px;width:73px;height:35px;background:#c8c8c8;border-radius:3px;color:#fff;font-family:"Arimo",sans-serif;font-weight:700;font-size:14px;display:flex;align-items:center;justify-content:center}
.account{top:99px;font-family:"Rokkitt",serif;font-size:16px;letter-spacing:.5px;color:var(--text)}

/* nav */
.main-nav{left:20px;top:171px;width:1167px;height:58px;border-top:1px solid var(--rule);border-bottom:1px solid var(--rule)}
.nav-item{position:absolute;top:13px;font-family:"Rokkitt",serif;font-size:25px;color:var(--ink)}

/* seo banner */
.seo-banner{left:22px;top:243px;width:844px;height:225px;border:1px solid #e6c6e2;border-radius:6px;overflow:hidden;background:linear-gradient(180deg,var(--pink-1),var(--pink-2))}
.page-title{position:absolute;left:101px;top:11px;font-family:"Rokkitt",serif;font-size:32px;color:var(--plum-dark)}
.title-rule{position:absolute;left:91px;top:54px;width:693px;border-top:1px dotted #8a6a86}
.seo-copy{position:absolute;left:101px;top:70px;width:680px;font-family:"Arimo",sans-serif;color:#6a6a6a;line-height:1}
.seo-copy p{margin-bottom:11px;white-space:nowrap}
.s1{font-size:13px}.s2{font-size:16px}.s3{font-size:19px}.s4{font-size:22px}.s5{font-size:26px}

/* featured */
.featured{left:884px;top:243px;width:300px;height:226px;border:2px solid var(--featured);border-radius:6px;overflow:hidden;background:#fff}
.featured-head{height:33px;background:var(--featured);color:var(--gold);font-family:"Oswald",sans-serif;font-weight:700;font-size:19px;padding:3px 0 0 10px;letter-spacing:.5px}
.featured-copy{position:absolute;left:24px;top:66px;font-family:"Oswald",sans-serif;font-weight:700;font-size:33px;line-height:1;color:#fff;text-shadow:-2px -2px 0 #6b5a5f,2px -2px 0 #6b5a5f,-2px 2px 0 #6b5a5f,2px 2px 0 #6b5a5f}
.featured-cards{position:absolute;left:134px;top:56px;width:152px;height:112px;border-radius:4px;background:linear-gradient(135deg,#e64a3a,#6cc04a 45%,#3aa0d8 70%,#f3b6c6)}

/* toolbar */
.sort{left:38px;top:496px;font-family:"Rokkitt",serif;font-size:20px;color:var(--ink)}
.sort-opt{top:499px;font-family:"Rokkitt",serif;font-size:16px;color:var(--muted)}
.pager-num{top:497px;font-family:"Open Sans",sans-serif;font-size:15px;color:var(--teal)}
.pager-num.current{color:#666}

/* filters */
.filter-title{left:36px;top:570px;font-family:"Rokkitt",serif;font-size:21px;color:var(--ink);display:flex;align-items:center;gap:10px}
.swatches{left:51px;top:609px;list-style:none}
.swatches li{height:24.3px;display:flex;align-items:center;gap:10px;font-size:14.5px;color:var(--text)}
.dot{width:18px;height:18px;border-radius:50%;border:1px solid rgba(0,0,0,.15)}

/* products */
.card{top:559px;width:269px;height:320px;background:var(--card);border:1px solid #ddd;border-radius:5px}
.card-art{position:absolute}
.quick-view{position:absolute;left:50%;top:252px;transform:translateX(-50%);width:116px;height:32px;border-radius:5px;background:linear-gradient(180deg,#ffe78a,#f3bf28);border:1px solid #d9a920;font-family:"Arimo",sans-serif;font-weight:700;font-size:14px;color:#4a3a10;display:flex;align-items:center;justify-content:center}
</style>
</head>
<body>
<div class="page">

  <div class="abs utility-bar">
    <div class="utility-item" style="left:36px">
      <svg width="22" height="16" viewBox="0 0 22 16"><rect x="0" y="2" width="13" height="10" fill="#555"/><path d="M13 5h5l4 4v3h-9z" fill="#555"/><circle cx="4" cy="13" r="2.5" fill="#555"/><circle cx="17" cy="13" r="2.5" fill="#555"/></svg>
      <span>FREE SHIPPING on orders over $150 - no coupon needed!</span>
    </div>
    <div class="utility-sep" style="left:470px"></div>
    <div class="utility-item" style="left:486px">
      <svg width="20" height="16" viewBox="0 0 20 16"><path d="M2 1h16a2 2 0 0 1 2 2v7a2 2 0 0 1-2 2H8l-5 4v-4H2a2 2 0 0 1-2-2V3a2 2 0 0 1 2-2z" fill="#555"/></svg>
      <span>Live Help</span>
    </div>
    <div class="utility-sep" style="left:593px"></div>
    <div class="utility-item" style="left:612px">
      <svg width="22" height="16" viewBox="0 0 22 16"><path d="M1 5c0-3 20-3 20 0v2h-5V5H6v2H1z" fill="#555"/><rect x="4" y="8" width="14" height="7" rx="2" fill="#555"/></svg>
      <span>555.010.4821</span>
    </div>
    <div class="utility-sep" style="left:760px"></div>
    <div class="utility-item" style="left:775px">
      <svg width="18" height="18" viewBox="0 0 18 18"><path d="M1 1h8l8 8-8 8-8-8z" fill="#555"/><circle cx="5" cy="5" r="1.6" fill="#f2f2f2"/></svg>
      <span>Become a Designer · Earn Commission</span>
    </div>
  </div>

  <header>
    <div class="abs brand">
      <div class="brand-mark"></div>
      <div class="brand-name">Party Wren</div>
    </div>
    <div class="abs search"><div class="search-btn">search</div></div>
    <div class="abs account" style="left:837px">LOGIN</div>
    <div class="abs account" style="left:900px">CREATE ACCOUNT</div>
    <svg class="abs" style="left:1052px;top:96px" width="24" height="22" viewBox="0 0 24 22"><path d="M0 2h4l3 12h13l3-9H6" fill="none" stroke="#666" stroke-width="2.4"/><circle cx="9" cy="19" r="2" fill="#666"/><circle cx="18" cy="19" r="2" fill="#666"/></svg>
    <div class="abs account" style="left:1088px;top:96px;font-size:19px">0</div>
  </header>

  <nav class="abs main-nav">
    <span class="nav-item" style="left:24px">Wedding</span>
    <span class="nav-item" style="left:170px">Party</span>
    <span class="nav-item" style="left:274px">Baby and Kids</span>
    <span class="nav-item" style="left:470px">Holiday</span>
    <span class="nav-item" style="left:600px">Graduation</span>
    <span class="nav-item" style="left:770px">Business</span>
    <span class="nav-item" style="left:910px">Stationery</span>
  </nav>

  <section class="abs seo-banner">
    <svg class="abs" style="left:0;top:0" width="844" height="225" viewBox="0 0 844 225">
      <path d="M0 0h88C50 20 20 50 0 90z" fill="var(--plum)"/>
      <path d="M0 0h70C40 18 16 42 0 72z" fill="#b866ae" opacity=".6"/>
      <path d="M844 20C830 110 800 180 750 225h94z" fill="var(--plum)"/>
      <path d="M844 60C836 130 818 185 790 225h54z" fill="#7d3578" opacity=".5"/>
    </svg>
    <h1 class="page-title">Page Heading</h1>
    <div class="title-rule"></div>
    <div class="seo-copy">
      <p><span class="s3">Lorem ipsum</span> <span class="s2">dolor sit amet,</span> &nbsp;<span class="s4">consectetur</span> <span class="s2">adipiscing</span> <span class="s3">elit.</span></p>
      <p><span class="s4">Vestibulum</span> <span class="s3">ut urna massa,</span> <span class="s2">tempus</span> <span class="s3">lacinia purus.</span></p>
      <p><span class="s2">Proin adipiscing</span> <span class="s4">sem non</span> <span class="s2">purus</span> <span class="s3">dapibus laoreet et</span> <span class="s2">vel odio.</span></p>
      <p><span class="s3">Cras volutpat</span> <span class="s2">arcu sed</span> <span class="s3">justo aliquet et auctor est euismod.</span></p>
    </div>
  </section>

  <aside class="abs featured">
    <div class="featured-head">FEATURED</div>
    <div class="featured-cards" role="img" aria-label="Fanned stack of colourful printed invitation proofs"></div>
    <div class="featured-copy">Free<br>Unlimited<br>Proofs</div>
  </aside>

  <div class="abs sort">Sort By:</div>
  <div class="abs sort-opt" style="left:128px">Price</div>
  <div class="abs sort-opt" style="left:186px">Name</div>
  <div class="abs sort-opt" style="left:253px">Vendor</div>

  <svg class="abs" style="left:945px;top:496px" width="24" height="24" viewBox="0 0 24 24"><circle cx="12" cy="12" r="12" fill="#cdc4c6"/><path d="M17 12H7m4-4-4 4 4 4" stroke="#fff" stroke-width="2.4" fill="none"/></svg>
  <span class="abs pager-num current" style="left:979px">1</span>
  <span class="abs pager-num" style="left:999px">2</span>
  <span class="abs pager-num" style="left:1019px">3</span>
  <span class="abs pager-num" style="left:1039px">4</span>
  <span class="abs pager-num" style="left:1059px">5</span>
  <span class="abs pager-num" style="left:1079px">6</span>
  <span class="abs pager-num" style="left:1099px">7</span>
  <span class="abs pager-num" style="left:1119px">8</span>
  <span class="abs pager-num" style="left:1139px">9</span>
  <svg class="abs" style="left:1158px;top:496px" width="24" height="24" viewBox="0 0 24 24"><circle cx="12" cy="12" r="12" fill="var(--teal)"/><path d="M7 12h10m-4-4 4 4-4 4" stroke="#fff" stroke-width="2.4" fill="none"/></svg>

  <div class="abs filter-title">
    <svg width="8" height="12" viewBox="0 0 8 12"><path d="M0 0l8 6-8 6z" fill="var(--ink)"/></svg>
    Filter By Color
  </div>
  <ul class="abs swatches">
    <li><span class="dot" style="background:#2a2a2a"></span>Black</li>
    <li><span class="dot" style="background:#4a86e8"></span>Blue</li>
    <li><span class="dot" style="background:#8a6a58"></span>Brown</li>
    <li><span class="dot" style="background:#f4b400"></span>Gold</li>
    <li><span class="dot" style="background:#7ed37e"></span>Green</li>
    <li><span class="dot" style="background:#c8c8c8"></span>Grey</li>
    <li><span class="dot" style="background:#f4f0de"></span>Ivory</li>
    <li><span class="dot" style="background:#ff9c4a"></span>Orange</li>
    <li><span class="dot" style="background:#f9b3dc"></span>Pink</li>
    <li><span class="dot" style="background:#7a2a6a"></span>Purple</li>
  </ul>

  <div class="abs card" style="left:336px">
    <div class="card-art" role="img" aria-label="Pirate party birthday invitation with colourful tiled panels" style="left:35px;top:0;width:196px;height:268px;background:linear-gradient(160deg,#6cc04a,#e63a2e 35%,#f3a21a 60%,#3aa0d8)"></div>
    <div class="quick-view">Quick View</div>
  </div>
  <div class="abs card" style="left:626px">
    <div class="card-art" role="img" aria-label="Superstar birthday invitation with photo, starry green border and blue name band" style="left:36px;top:0;width:196px;height:268px;background:linear-gradient(180deg,#5cb83c,#7cc850 45%,#2aa0d8 55%,#f7b52a 75%,#f39a1a)"></div>
    <div class="quick-view">Quick View</div>
  </div>
  <div class="abs card" style="left:917px">
    <div class="card-art" role="img" aria-label="Orange triceratops shaped birthday invitation" style="left:0;top:0;width:267px;height:168px;background:#fff;border-radius:5px 5px 0 0"></div>
    <div class="card-art" aria-hidden="true" style="left:16px;top:10px;width:238px;height:150px;border-radius:40% 50% 30% 40%;background:radial-gradient(circle at 60% 45%,#ffc63a,#f5a623 70%)"></div>
    <div class="quick-view">Quick View</div>
  </div>

</div>
</body>
</html>
```